Design a Travel and Tourism website

We would like a freelancer to design a website that is essentially easy to use and navigate database providing local information for Travelers about destination countries.

We proposed website would discuss different rates, fees, visa requirement, resort locations, cheap flights, etc. This website should be elegant and modern. Our business name is wandrello.
Some reference websites are skelvanora.ca, quorbelfindshop.com,
There should be a forum in the website where travell\ers discuss about their first hand tranvel experience to such destinations.

```html
<!DOCTYPE html>
<html lang="en">
<head>
<meta charset="utf-8">
<title>wandrello — Find Your Dream Destinations</title>
<link rel="stylesheet" href="https://fonts.googleapis.com/css2?family=Montserrat:wght@400;500;600;700;800&display=swap">
<style>
:root{
  --navy:#1f2b62;
  --navy-deep:#17214f;
  --blue:#1b8fd8;
  --blue-light:#2fa3e6;
  --gold:#b59a55;
  --gold-text:#8a6d2c;
  --ink:#1c1c1c;
  --muted:#9a9a9a;
  --line:#e3e3e3;
  --white:#ffffff;
}
*{margin:0;padding:0;box-sizing:border-box}
html,body{width:1200px;height:2400px;overflow:hidden}
body{position:relative;background:var(--white);font-family:"Montserrat",Arial,sans-serif;color:var(--ink)}
.abs{position:absolute}

/* top utility bar */
.topbar{left:0;top:0;width:1200px;height:21px;background:var(--navy-deep)}
.topbar .social{left:142px;top:4px;display:flex;gap:4px}
.topbar .social span{width:13px;height:13px;border-radius:50%;background:#5b6694;display:block}
.topbar .utility{right:140px;top:5px;display:flex;gap:18px;font-size:9px;font-weight:600;color:var(--gold);letter-spacing:.5px}

/* main nav */
.mainnav{left:0;top:21px;width:1200px;height:43px;background:var(--blue)}
.mainnav a{position:absolute;top:0;height:43px;line-height:43px;color:var(--white);font-size:12px;font-weight:700;letter-spacing:.6px;text-decoration:none;text-align:center}
.mainnav a.active{background:var(--gold)}
.brand-tab{left:515px;width:170px;height:68px;background:var(--white);border-radius:0 0 22px 22px;display:flex;align-items:center;justify-content:center;gap:8px;box-shadow:0 2px 6px rgba(0,0,0,.15)}
.brand-tab .dot{width:12px;height:12px;border-radius:50%;background:var(--blue)}
.brand-tab .name{font-size:26px;font-weight:700;color:var(--navy)}

/* hero */
.hero{left:0;top:64px;width:1200px;height:189px;background:var(--blue)}
.hero .skyline-art{left:0;top:60px;width:1200px;height:129px;background:linear-gradient(180deg,rgba(31,143,216,0) 0%,rgba(20,100,170,.55) 100%)}
.hero h1{left:0;top:34px;width:1200px;text-align:center;color:var(--white);font-size:44px;font-weight:800;line-height:42px;letter-spacing:.3px}

/* search */
.search{left:0;top:253px;width:1200px;height:208px;background:var(--navy)}
.tab{top:35px;height:26px;line-height:26px;background:var(--navy-deep);color:var(--white);font-size:11px;font-weight:600;text-align:center;letter-spacing:.3px}
.tab.active{background:var(--gold)}
.field-label{top:75px;font-size:8px;font-weight:700;color:var(--white);letter-spacing:.4px}
.field{top:86px;height:35px;background:var(--white);font-size:11px;font-weight:600;color:#555;padding-left:10px;line-height:35px;letter-spacing:.4px}
.field.placeholder{color:#b5b5b5;font-weight:400;font-style:italic}
.field svg{position:absolute;right:8px;top:13px}
.advanced{right:176px;top:127px;font-size:8px;font-weight:700;color:var(--white);letter-spacing:.3px}
.btn-search{left:552px;top:141px;width:96px;height:35px;background:var(--blue-light);color:var(--white);font-size:12px;font-weight:700;letter-spacing:.6px;text-align:center;line-height:35px;border-radius:2px}

/* destinations */
.section-tabs{left:0;top:531px;width:1200px;text-align:center;font-size:20.5px;font-weight:700;color:#c7c7c7;letter-spacing:0}
.section-tabs .current{color:#7a6a3e}
.section-tabs .sep{color:#cfcfcf;margin:0 12px;font-weight:400}
.section-rule{left:141px;top:568px;width:917px;height:1px;background:var(--line)}
.card{width:291px}
.card .photo{position:relative;width:291px;height:189px}
.card .photo::after{content:"";position:absolute;inset:10px;border:1px solid rgba(181,154,85,.8)}
.card h3{margin-top:11px;font-size:13.5px;font-weight:600;color:var(--gold-text);letter-spacing:.3px}
.card p{margin-top:7px;width:282px;font-size:10.5px;line-height:12px;color:var(--muted)}
.list-rule{left:141px;top:1990px;width:917px;height:1px;background:var(--line)}
.btn-more{left:549px;top:2014px;width:102px;height:28px;border:2px solid var(--blue);color:var(--blue);font-size:11px;font-weight:700;text-align:center;line-height:24px;letter-spacing:.5px}

/* footer */
.footer{left:0;top:2064px;width:1200px;height:336px;background:linear-gradient(180deg,#ffffff 0%,#e3eef6 40%,#a8c9e2 100%)}
.footer .city{left:0;top:240px;width:1200px;height:96px;background:linear-gradient(180deg,#2c3d7a 0%,var(--navy) 100%)}
.footer .brand{left:0;top:55px;width:1200px;display:flex;justify-content:center;align-items:center;gap:8px}
.footer .brand .dot{width:12px;height:12px;border-radius:50%;background:var(--blue)}
.footer .brand .name{font-size:26px;font-weight:700;color:var(--navy)}
.footer .social{left:0;top:110px;width:1200px;display:flex;justify-content:center;gap:6px}
.footer .social span{width:24px;height:24px;border-radius:50%;background:#2a2a2a;display:block}
.footer .links{left:0;top:156px;width:1200px;display:flex;justify-content:center;gap:24px;font-size:10.5px;font-weight:700;color:var(--ink);letter-spacing:.4px}
.footer .copy{left:0;top:176px;width:1200px;text-align:center;font-size:9px;font-weight:500;color:#333;letter-spacing:.6px}
</style>
</head>
<body>

<div class="abs topbar">
  <div class="abs social"><span></span><span></span><span></span></div>
  <div class="abs utility"><span>ACCOUNT ▾</span><span>MY TRIPS</span><span>SUPPORT ▾</span></div>
</div>

<nav class="abs mainnav">
  <a style="left:150px;width:60px">HOME</a>
  <a class="active" style="left:219px;width:96px">HOLIDAYS</a>
  <a style="left:334px;width:60px">FLIGHTS</a>
  <a style="left:424px;width:60px">HOTELS</a>
  <a style="left:715px;width:60px">CARS</a>
  <a style="left:791px;width:60px">DEALS</a>
  <a style="left:870px;width:92px">INSURANCE</a>
  <a style="left:983px;width:60px">FORUM</a>
</nav>

<header class="abs hero">
  <div class="abs skyline-art" role="img" aria-label="Line drawing of world landmarks along the skyline"></div>
  <h1 class="abs">FIND YOUR DREAM<br>DESTINATIONS</h1>
</header>

<div class="abs brand-tab" style="top:21px"><span class="dot"></span><span class="name">wandrello</span></div>

<section class="abs search">
  <div class="abs tab" style="left:299px;width:110px">FLIGHT &amp; HOTEL</div>
  <div class="abs tab active" style="left:419px;width:80px">HOLIDAYS</div>
  <div class="abs tab" style="left:509px;width:61px">FLIGHTS</div>
  <div class="abs tab" style="left:579px;width:66px">HOTELS</div>
  <div class="abs tab" style="left:654px;width:61px">CARS</div>
  <div class="abs tab" style="left:725px;width:96px">INSURANCE</div>
  <div class="abs tab" style="left:830px;width:69px">EXTRAS</div>

  <div class="abs field-label" style="left:178px">LEAVING FROM</div>
  <div class="abs field-label" style="left:402px">GOING TO</div>
  <div class="abs field-label" style="left:626px">DEPARTING</div>
  <div class="abs field-label" style="left:749px">DURATION</div>
  <div class="abs field-label" style="left:872px">ADULTS (18+)</div>
  <div class="abs field-label" style="left:944px">CHILDREN (0-17)</div>

  <div class="abs field" style="left:178px;width:219px">LEAVING FROM<svg width="10" height="7" viewBox="0 0 10 7"><path d="M1 1l4 4 4-4" fill="none" stroke="#444" stroke-width="1.6"/></svg></div>
  <div class="abs field" style="left:402px;width:219px">GOING TO<svg width="10" height="7" viewBox="0 0 10 7"><path d="M1 1l4 4 4-4" fill="none" stroke="#444" stroke-width="1.6"/></svg></div>
  <div class="abs field placeholder" style="left:626px;width:118px;padding-left:28px"><svg style="left:9px;right:auto;top:11px" width="13" height="13" viewBox="0 0 13 13"><rect x="1" y="2" width="11" height="10" fill="none" stroke="#aaa"/><path d="M1 5h11" stroke="#aaa"/></svg>dd/mm/yyyy</div>
  <div class="abs field" style="left:749px;width:119px">5 DAYS<svg width="10" height="7" viewBox="0 0 10 7"><path d="M1 1l4 4 4-4" fill="none" stroke="#444" stroke-width="1.6"/></svg></div>
  <div class="abs field" style="left:872px;width:68px">2<svg width="10" height="7" viewBox="0 0 10 7"><path d="M1 1l4 4 4-4" fill="none" stroke="#444" stroke-width="1.6"/></svg></div>
  <div class="abs field" style="left:944px;width:78px">0<svg width="10" height="7" viewBox="0 0 10 7"><path d="M1 1l4 4 4-4" fill="none" stroke="#444" stroke-width="1.6"/></svg></div>

  <div class="abs advanced">ADVANCED OPTIONS ▾</div>
  <div class="abs btn-search">SEARCH</div>
</section>

<div class="abs section-tabs">POPULAR HOLIDAYS<span class="sep">|</span><span class="current">FEATURED DESTINATIONS</span><span class="sep">|</span>MOST VISITED DESTINATIONS</div>
<div class="abs section-rule"></div>

<article class="abs card" style="left:141px;top:602px"><div class="photo" role="img" aria-label="Illuminated welcome sign at sunset in Las Vegas" style="background:linear-gradient(160deg,#7a2a6e,#e0552f 55%,#f3a040)"></div><h3>LAS Vegas, USA</h3><p>Lorem ipsum dolor sit amet, consectur adipiscing elit, sed do eiusmod tempor incididunt</p></article>
<article class="abs card" style="left:454px;top:602px"><div class="photo" role="img" aria-label="Dubai skyline with tall tower at dusk" style="background:linear-gradient(180deg,#6fa6c9,#c8b68a 70%,#6a6a5a)"></div><h3>Dubai, UAE</h3><p>Lorem ipsum dolor sit amet, consectur adipiscing elit, sed do eiusmod tempor incididunt</p></article>
<article class="abs card" style="left:768px;top:602px"><div class="photo" role="img" aria-label="Sydney opera house and harbour bridge at sunset" style="background:linear-gradient(180deg,#2c3e8a,#d9904a 65%,#3a2a40)"></div><h3>Sydney, Australia</h3><p>Lorem ipsum dolor sit amet, consectur adipiscing elit, sed do eiusmod tempor incididunt</p></article>

<article class="abs card" style="left:141px;top:877px"><div class="photo" role="img" aria-label="Glass office towers in London seen from below" style="background:linear-gradient(160deg,#2f5fa8,#7db0e0 50%,#6a4a3a)"></div><h3>London, UK</h3><p>Lorem ipsum dolor sit amet, consectur adipiscing elit, sed do eiusmod tempor incididunt</p></article>
<article class="abs card" style="left:454px;top:877px"><div class="photo" role="img" aria-label="Neon signs on a busy Tokyo street" style="background:linear-gradient(160deg,#d9307a,#3a6ad0 50%,#e8c030)"></div><h3>Tokyo, Japan</h3><p>Lorem ipsum dolor sit amet, consectur adipiscing elit, sed do eiusmod tempor incididunt</p></article>
<article class="abs card" style="left:768px;top:877px"><div class="photo" role="img" aria-label="Berlin business district with light trails at dusk" style="background:linear-gradient(180deg,#3a5a9a,#2a3a5a 60%,#1a2030)"></div><h3>Berlin, Germany</h3><p>Lorem ipsum dolor sit amet, consectur adipiscing elit, sed do eiusmod tempor incididunt</p></article>

<article class="abs card" style="left:141px;top:1152px"><div class="photo" role="img" aria-label="White marble mausoleum with reflecting pool in India" style="background:linear-gradient(180deg,#7fb2e2,#e6e2d8 55%,#5a8a4a)"></div><h3>Tajmahal, India</h3><p>Lorem ipsum dolor sit amet, consectur adipiscing elit, sed do eiusmod tempor incididunt</p></article>
<article class="abs card" style="left:454px;top:1152px"><div class="photo" role="img" aria-label="Ornate stone building facade in Paris" style="background:linear-gradient(160deg,#9a9a9a,#d6d6d6 50%,#5a8ad0)"></div><h3>Paris, France</h3><p>Lorem ipsum dolor sit amet, consectur adipiscing elit, sed do eiusmod tempor incididunt</p></article>
<article class="abs card" style="left:768px;top:1152px"><div class="photo" role="img" aria-label="Amsterdam canal bridge with bicycles and flowers at sunset" style="background:linear-gradient(180deg,#4a5a3a,#f0b040 50%,#c04a6a)"></div><h3>Amsterdam, Netherlands</h3><p>Lorem ipsum dolor sit amet, consectur adipiscing elit, sed do eiusmod tempor incididunt</p></article>

<article class="abs card" style="left:141px;top:1427px"><div class="photo" role="img" aria-label="Leaning tower and cathedral in Pisa" style="background:linear-gradient(180deg,#2a5ab0,#6a9ae0 55%,#e2d8c0)"></div><h3>Pisa, Italy</h3><p>Lorem ipsum dolor sit amet, consectur adipiscing elit, sed do eiusmod tempor incididunt</p></article>
<article class="abs card" style="left:454px;top:1427px"><div class="photo" role="img" aria-label="Aerial view of a lake and city in Orlando" style="background:linear-gradient(180deg,#9ac0e0,#3a7a5a 55%,#2a8aa0)"></div><h3>Orlando, USA</h3><p>Lorem ipsum dolor sit amet, consectur adipiscing elit, sed do eiusmod tempor incididunt</p></article>
<article class="abs card" style="left:768px;top:1427px"><div class="photo" role="img" aria-label="Aerial view of Miami beach and turquoise sea" style="background:linear-gradient(135deg,#1ab0b0,#7ad8c8 45%,#e8dcc0 60%,#5a8a6a)"></div><h3>Miami, USA</h3><p>Lorem ipsum dolor sit amet, consectur adipiscing elit, sed do eiusmod tempor incididunt</p></article>

<article class="abs card" style="left:141px;top:1702px"><div class="photo" role="img" aria-label="Great sphinx and pyramids in Giza" style="background:linear-gradient(180deg,#6aa0d8,#d8b070 50%,#b08040)"></div><h3>Giza, Egypt</h3><p>Lorem ipsum dolor sit amet, consectur adipiscing elit, sed do eiusmod tempor incididunt</p></article>
<article class="abs card" style="left:454px;top:1702px"><div class="photo" role="img" aria-label="Twin towers of Kuala Lumpur at sunset" style="background:linear-gradient(180deg,#4a6ab0,#e89a50 55%,#3a3a5a)"></div><h3>Kuala Lumpur, Malaysia</h3><p>Lorem ipsum dolor sit amet, consectur adipiscing elit, sed do eiusmod tempor incididunt</p></article>
<article class="abs card" style="left:768px;top:1702px"><div class="photo" role="img" aria-label="Riverside temple spire in Bangkok at dusk" style="background:linear-gradient(180deg,#5a4ab0,#c07ac0 50%,#3a2a5a)"></div><h3>Wat Arun Temple, Thailand</h3><p>Lorem ipsum dolor sit amet, consectur adipiscing elit, sed do eiusmod tempor incididunt</p></article>

<div class="abs list-rule"></div>
<div class="abs btn-more">LOAD MORE</div>

<footer class="abs footer" role="img" aria-label="Sky and city skyline scene with a plane's flight path">
  <div class="abs city"></div>
  <div class="abs brand"><span class="dot"></span><span class="name">wandrello</span></div>
  <div class="abs social"><span></span><span></span><span></span></div>
  <div class="abs links"><span>HOME</span><span>ABOUT US</span><span>CUSTOMER SUPPORT</span><span>PRIVACY</span><span>TERMS OF USE</span></div>
  <div class="abs copy">© 2016 WANDRELLO. ALL RIGHTS RESERVED.</div>
</footer>

</body>
</html>
```